A4 Wholesale Catalogue for a Hardware Supply Company

We are a tarpaulin manufacture and supply company. We need a A4 multi page catalogue to be used as a selling tool for our wholesale customers. We want the catalogue to be easily understandable but also eye catching.

This catalogue will be used by local hardware stores to sell our products to their account customers. The idea of this catalogue is to enable the hardware store to have a snapshot of our products that will be relevant to their customers whom are largely builders. This will be not be given out to their customer and will be used only in store as a selling tool.

Industry/Entity Type

Building

Font styles to use
Serif

Requirements
Must have
• Detail as per supplied brief.
• Photos
• Branding
Should not have
• To many tables

```html
<!DOCTYPE html>
<html lang="en">
<head>
<meta charset="utf-8">
<title>Tarpaulin Range – Wholesale Catalogue</title>
<link rel="stylesheet" href="https://fonts.googleapis.com/css2?family=Questrial&display=swap">
<style>
:root{
  --bg:#e9e6e1;
  --blue:#3f68b1;
  --blue-deep:#3560a9;
  --row:#ececec;
  --row-alt:#f4f4f4;
  --line:#ffffff;
  --head:#a8a8a8;
  --ink:#333333;
  --ink-soft:#555555;
  --white:#ffffff;
}
*{box-sizing:border-box;margin:0;padding:0}
html,body{width:1200px;height:1200px;overflow:hidden;background:var(--bg)}
body{font-family:"Questrial",sans-serif;color:var(--ink);position:relative}
.page{
  position:absolute;left:190px;top:20px;width:914px;height:1292px;
  transform:scale(.8978);transform-origin:0 0;
  background:var(--blue);overflow:hidden;
  box-shadow:0 4px 14px rgba(0,0,0,.25);
}
.warehouse-photo{
  position:absolute;left:0;top:0;width:914px;height:700px;
  background:
    linear-gradient(180deg,rgba(63,104,177,0) 45%,var(--blue) 100%),
    linear-gradient(100deg,#8a8f98 0%,#b9bcc2 20%,#6f7f9e 40%,#c7c9cc 60%,#8b8e94 80%,#9aa3b5 100%);
}
.product-panel{
  position:absolute;left:209px;top:219px;width:661px;height:167px;
  background:var(--white);border-radius:12px 12px 0 0;
  display:grid;grid-template-columns:repeat(4,1fr);
}
.product{display:flex;flex-direction:column;align-items:center}
.product-shot{width:130px;height:105px;margin-top:14px;border-radius:8px;transform:skewY(-8deg)}
.shot-silver{background:linear-gradient(135deg,#a9abad,#6e7174)}
.shot-forest{background:linear-gradient(135deg,#3f7a58,#1f4d35)}
.shot-green{background:linear-gradient(135deg,#3e9a5c,#23703e)}
.shot-blue{background:linear-gradient(135deg,#3b5bc8,#1c3290)}
.product-name{font-size:19px;margin-top:18px;color:var(--ink)}
table{border-collapse:collapse;table-layout:fixed;position:absolute;left:44px;width:826px}
td,th{font-weight:normal;text-align:center;border-bottom:1px solid var(--line);border-right:1px solid var(--line)}
td:last-child,th:last-child{border-right:none}
.feature-table{top:386px}
.feature-table td{height:27px;font-size:14px;background:var(--row);line-height:1.1}
.feature-table td.label{text-align:left;padding-left:14px;background:rgba(255,255,255,.82);color:var(--ink-soft)}
.feature-table .ticks{font-size:17px;letter-spacing:1px;color:#222}
.feature-table tr.extra td{height:53px;vertical-align:top;padding-top:7px;text-align:left;padding-left:13px;font-size:13.5px;line-height:.95}
.feature-table tr.extra td.label{font-size:14px;line-height:1.1}
.size-table{top:668px}
.size-table th{background:var(--head);color:var(--white);height:52px;font-size:13px;line-height:1.05}
.size-table th b{display:block;font-weight:bold}
.size-table td{height:26.9px;font-size:14px;background:var(--row)}
.size-table td.size{text-align:left;padding-left:9px}
.size-table td.area{text-align:right;padding-right:5px}
.footer{
  position:absolute;left:0;top:1248px;width:914px;height:44px;background:var(--white);
  display:flex;align-items:center;justify-content:center;font-size:19px;color:var(--ink);gap:10px
}
</style>
</head>
<body>
<div class="page">
  <div class="warehouse-photo" role="img" aria-label="Warehouse shelving stocked with packaged tarpaulins"></div>

  <div class="product-panel">
    <div class="product"><div class="product-shot shot-silver" role="img" aria-label="Packaged silver and green poly tarpaulin"></div><div class="product-name">240gsm Poly</div></div>
    <div class="product"><div class="product-shot shot-forest" role="img" aria-label="Packaged green and white poly tarpaulin"></div><div class="product-name">300gsm Poly</div></div>
    <div class="product"><div class="product-shot shot-green" role="img" aria-label="Packaged green PVC tarpaulin"></div><div class="product-name">550gsm PVC</div></div>
    <div class="product"><div class="product-shot shot-blue" role="img" aria-label="Packaged blue PVC tarpaulin"></div><div class="product-name">650gsm PVC</div></div>
  </div>

  <table class="feature-table">
    <colgroup><col style="width:165px"><col><col><col><col></colgroup>
    <tr><td class="label">Tear Resistance</td><td class="ticks">✓✓✓</td><td class="ticks">✓✓✓✓</td><td class="ticks">✓✓✓✓✓</td><td class="ticks">✓✓✓✓✓✓</td></tr>
    <tr><td class="label">Abrasion Resistance</td><td class="ticks">✓✓✓</td><td class="ticks">✓✓✓✓</td><td class="ticks">✓✓✓✓✓</td><td class="ticks">✓✓✓✓✓✓</td></tr>
    <tr><td class="label">Puncture Resistance</td><td class="ticks">✓✓✓</td><td class="ticks">✓✓✓</td><td class="ticks">✓✓✓✓✓</td><td class="ticks">✓✓✓✓✓✓</td></tr>
    <tr><td class="label">Repairable</td><td>-</td><td>-</td><td colspan="2">Easily repaired with head weld patch</td></tr>
    <tr><td class="label">Waterproof</td><td class="ticks">✓✓✓</td><td class="ticks">✓✓✓</td><td class="ticks">✓✓✓</td><td class="ticks">✓✓✓</td></tr>
    <tr><td class="label">UV Treated</td><td class="ticks">✓✓✓</td><td class="ticks">✓✓✓</td><td class="ticks">✓✓✓</td><td class="ticks">✓✓✓</td></tr>
    <tr><td class="label">Centre Tie Downs</td><td>-</td><td>-</td><td class="ticks">✓✓✓</td><td class="ticks">✓✓✓</td></tr>
    <tr><td class="label">Sizes available up to</td><td>250m2 (12x21m)</td><td>180m2 (12x15m)</td><td>110m2 (8x14)</td><td>80m2 (7x11m)</td></tr>
    <tr class="extra"><td class="label">Additional Features</td><td>Easy to fold &amp;<br>manoeuvre</td><td>Easy to fold &amp;<br>manoeuvre</td><td>Less prone to<br>flapping</td><td>Less prone to<br>flapping &amp; fire<br>retardant</td></tr>
  </table>

  <table class="size-table">
    <colgroup><col style="width:111px"><col style="width:54px"><col><col><col><col></colgroup>
    <tr><th>Sizes</th><th>SQ.M<br>Cove<br>rage</th><th><b>240gsm Poly</b>Silver/Green<br>Range Code - SG</th><th><b>300gsm Poly</b>Green/White<br>Range Code - GW</th><th><b>550gsm PVC</b>Green<br>Range Code - VG</th><th><b>650gsm PVC</b>Blue<br>Range Code - VB</th></tr>
    <tr><td class="size">6.0m x 9.0m</td><td class="area">54m2</td><td>12.5kg</td><td>16.0kg</td><td>29.5kg</td><td>35.0kg</td></tr>
    <tr><td class="size">6.0m x 12.0m</td><td class="area">72m2</td><td>17.5kg</td><td>22.5kg</td><td></td><td>47.0kg</td></tr>
    <tr><td class="size">7.0m x 12.0m</td><td class="area">84m2</td><td>20.0kg</td><td>25.0kg</td><td></td><td></td></tr>
    <tr><td class="size">7.2m x 9.0m</td><td class="area">64m2</td><td>15.5kg</td><td>19.0kg</td><td></td><td>41.5kg</td></tr>
    <tr><td class="size">7.2m x 11.0m</td><td class="area">79m2</td><td></td><td></td><td></td><td>51.0kg</td></tr>
    <tr><td class="size">7.5m x 15.0m</td><td class="area">112m2</td><td></td><td>33.5kg</td><td></td><td></td></tr>
    <tr><td class="size">8.0m x 10.0m</td><td class="area">80m2</td><td></td><td></td><td></td><td>52.0kg</td></tr>
    <tr><td class="size">8.0m x 14.0m</td><td class="area">112m2</td><td></td><td></td><td>61.5kg</td><td></td></tr>
    <tr><td class="size">9.0m x 9.0m</td><td class="area">84m2</td><td>19.5kg</td><td>25.0kg</td><td></td><td></td></tr>
    <tr><td class="size">9.0m x 12.0m</td><td class="area">108m2</td><td>24.0kg</td><td>32.5kg</td><td>59.5kg</td><td></td></tr>
    <tr><td class="size">9.0m x 15.0m</td><td class="area">135m2</td><td>32.5kg</td><td>40.5kg</td><td></td><td></td></tr>
    <tr><td class="size">9.0m x 18.0m</td><td class="area">162m2</td><td>38.5kg</td><td></td><td></td><td></td></tr>
    <tr><td class="size">10.0m x 12.0m</td><td class="area">120m2</td><td>28.5kg</td><td></td><td></td><td></td></tr>
    <tr><td class="size">12.0m x 12.0m</td><td class="area">144m2</td><td>34.5kg</td><td>43.0kg</td><td></td><td></td></tr>
    <tr><td class="size">12.0m x 15.0m</td><td class="area">180m2</td><td>43.0kg</td><td>54.0kg</td><td></td><td></td></tr>
    <tr><td class="size">12.0m x 18.0m</td><td class="area">216m2</td><td>51.5kg</td><td></td><td></td><td></td></tr>
    <tr><td class="size">15.0m x 15.0m</td><td class="area">225m2</td><td>60.5kg</td><td></td><td></td><td></td></tr>
    <tr><td class="size">12.0m x 21.0m</td><td class="area">252m2</td><td>60.5kg</td><td></td><td></td><td></td></tr>
  </table>

  <div class="footer"><span>14/8 Harbour Row</span><span>|</span><span>Millbrook NSW 2099</span><span>|</span><span>sales@ridgecovertarps.com.au</span></div>
</div>
</body>
</html>
```